Email Marketing Campaign Templates

Email drip childcare campaign designed to communicate with parents interested in services. We would like the template(s) to be created so that we can change the content as needed.I will add below collateral that we have used in the past as well as logo.
three to for templates 1.) welcome template 2/ things to bring 3) generic template
Target Market(s)
Parents and Millennials
Industry/Entity Type
Childcare
Colors
85cae6
0493ce
9bcb3c
add136
fefefe
faa54b
cadf82
86cae7
33a6d7
Requirements
Must have
- Photos of staff with children
Nice to have
- Photos

```html
<!DOCTYPE html>
<html lang="en">
<head>
<meta charset="utf-8">
<title>Bloomwell Early Education Center – Welcome</title>
<link href="https://fonts.googleapis.com/css2?family=Cabin+Sketch:wght@400;700&family=Fredoka:wght@500;600&family=Patrick+Hand&family=Quicksand:wght@500&display=swap" rel="stylesheet">
<style>
  :root{
    --page:#ececec;
    --paper:#f1f1ee;
    --leaf:#6cbd3e;
    --leaf-bright:#9bcb3c;
    --board-dark:#1f5a2a;
    --board:#2f7a38;
    --board-light:#3d8a46;
    --shirt:#9a95e2;
    --hair:#d8c08a;
    --sky:#0e8fd0;
    --sky-soft:#33a6d7;
    --navy:#0b3a5c;
    --orange:#faa54b;
    --white:#fefefe;
  }
  *{box-sizing:border-box;margin:0;padding:0}
  html,body{width:1200px;height:2161px;overflow:hidden}
  body{background:var(--page);position:relative}
  .flyer{position:absolute;left:144px;top:89px;width:915px;height:1981px;overflow:hidden;background:var(--paper)}

  /* header */
  .masthead{position:absolute;left:0;top:0;width:915px;height:302px;background:var(--paper)}
  .brand{position:absolute;left:110px;top:112px;display:flex;align-items:center;gap:20px}
  .brand-dot{width:58px;height:58px;border-radius:50%;background:var(--sky-soft)}
  .brand-name{font-family:"Fredoka",sans-serif;font-weight:600;font-size:72px;color:var(--sky-soft);line-height:1}
  .motto{position:absolute;left:610px;top:58px;border-left:8px solid var(--leaf);padding-left:24px;
    font-family:"Fredoka",sans-serif;font-weight:600;font-size:50px;line-height:66px;color:var(--leaf)}

  /* hero photo */
  .hero{position:absolute;left:0;top:302px;width:915px;height:657px;
    background:
      radial-gradient(ellipse 230px 150px at 50% 100%, var(--shirt) 0%, var(--shirt) 55%, rgba(154,149,226,0) 100%),
      radial-gradient(ellipse 120px 190px at 50% 52%, rgba(216,192,138,.75) 0%, rgba(216,192,138,0) 100%),
      radial-gradient(ellipse at 50% 55%, var(--board-light) 0%, var(--board) 45%, var(--board-dark) 100%)}

  /* welcome band */
  .welcome{position:absolute;left:0;top:959px;width:915px;height:202px;background:var(--leaf);text-align:center}
  .welcome-title{font-family:"Cabin Sketch",sans-serif;font-weight:700;font-size:132px;line-height:1;color:var(--white);padding-top:22px;letter-spacing:1px}
  .welcome-sub{font-family:"Quicksand",sans-serif;font-weight:500;font-size:24px;color:var(--white);letter-spacing:4px;margin-top:8px}

  /* features */
  .features{position:absolute;left:0;top:1161px;width:915px;height:648px;background:var(--sky)}
  .photo-dot{position:absolute;left:122px;width:218px;height:218px;border-radius:50%;border:9px solid var(--white)}
  .photo-dot.one{top:24px;background:radial-gradient(circle at 50% 45%, #d9c9b3, #8a7a66)}
  .photo-dot.two{top:210px;background:radial-gradient(circle at 50% 60%, #e0b25a, #6b6d70)}
  .photo-dot.three{top:410px;background:radial-gradient(circle at 45% 50%, #9fd06a, #3f7d3a)}
  .feature{position:absolute;left:402px;width:420px;color:var(--white)}
  .feature h2{font-family:"Cabin Sketch",sans-serif;font-weight:700;font-size:32px;letter-spacing:1px;line-height:1.1}
  .feature p{font-family:"Patrick Hand",cursive;font-size:17px;line-height:21px;margin-top:12px}
  .feature.approach{top:52px}
  .feature.village{top:236px}
  .feature.playful{top:400px}
  .rule{position:absolute;left:402px;width:172px;height:1px;background:rgba(255,255,255,.7)}
  .rule.a{top:206px}.rule.b{top:368px}
  .hours{position:absolute;right:40px;top:584px;width:385px;height:64px;background:var(--navy);
    border-radius:30px 22px 0 0;transform:skewX(-8deg);display:flex;align-items:center;justify-content:center}
  .hours span{transform:skewX(8deg);font-family:"Fredoka",sans-serif;font-weight:600;font-size:29px;color:var(--orange);letter-spacing:1px}

  /* footer */
  .contact{position:absolute;left:0;top:1809px;width:915px;height:172px;background:var(--leaf)}
  .contact-item{position:absolute;display:flex;align-items:center;gap:22px;
    font-family:"Fredoka",sans-serif;font-weight:600;font-size:26px;line-height:28px;color:var(--white)}
  .contact-item svg{flex:none}
  .contact-item.address{left:82px;top:30px}
  .contact-item.phone{left:82px;top:110px}
  .contact-item.email{left:480px;top:38px}
  .contact-item.web{left:480px;top:110px}
</style>
</head>
<body>
<main class="flyer">
  <header class="masthead">
    <div class="brand"><span class="brand-dot"></span><span class="brand-name">Bloomwell</span></div>
    <div class="motto">NARTURE<br>FLOURISH<br>GROW</div>
  </header>

  <section class="hero" role="img" aria-label="Photo: smiling girl with long blond braids in a lavender polo shirt standing in front of a green chalkboard decorated with chalk doodles of a plant, camera, flute, paint palette, globe, book and bicycle"></section>

  <section class="welcome">
    <h1 class="welcome-title">WELCOME</h1>
    <p class="welcome-sub">TO YOUR CHILD'S HAPPY PLACE.</p>
  </section>

  <section class="features">
    <div class="photo-dot one" role="img" aria-label="Teacher reading with a group of toddlers in a classroom"></div>
    <div class="photo-dot two" role="img" aria-label="Child building with colourful wooden blocks"></div>
    <div class="photo-dot three" role="img" aria-label="Young children drawing on a green wall"></div>

    <article class="feature approach">
      <h2>A WHOLE-CHILD APPROACH</h2>
      <p>At Bloomwell, we know that your child is so much more than what they know, so we use an educational approach that considers the whole child. They get to be who they are, and learn in a way that allows them to flourish.</p>
    </article>
    <span class="rule a"></span>
    <article class="feature village">
      <h2>WE BUILD THE VILLAGE</h2>
      <p>You've heard the saying, "It takes a village," here we strive to help you build a meaningful, supportive, community for you and your family.</p>
    </article>
    <span class="rule b"></span>
    <article class="feature playful">
      <h2>PLAYFUL AND PRACTICAL</h2>
      <p>At our center, we think it's possible to allow children to be playful, and flourish in their individual identities, while also fostering the development of necessary practical skills. We help each child develop confidence in themselves and respect for their peers through our unique teaching process.</p>
    </article>

    <div class="hours"><span>MON-FRI: 7AM-6PM</span></div>
  </section>

  <footer class="contact">
    <div class="contact-item address">
      <svg width="40" height="40" viewBox="0 0 40 40" aria-hidden="true"><circle cx="20" cy="20" r="20" fill="#fefefe"/><path d="M20 9c-4.4 0-8 3.4-8 7.8 0 5.6 8 14.2 8 14.2s8-8.6 8-14.2C28 12.4 24.4 9 20 9z" fill="#6cbd3e"/><circle cx="20" cy="17" r="3" fill="#fefefe"/></svg>
      <span>208 Linden Avenue,<br>Dayton, OH 45402</span>
    </div>
    <div class="contact-item phone">
      <svg width="40" height="40" viewBox="0 0 40 40" aria-hidden="true"><circle cx="20" cy="20" r="20" fill="#fefefe"/><path d="M14 10l4 1 2 6-3 2c1 3 3 5 6 6l2-3 6 2 1 4c-1 2-3 3-5 3-9-1-16-8-17-17 0-2 2-4 4-4z" fill="#6cbd3e"/></svg>
      <span>937.555.0148</span>
    </div>
    <div class="contact-item email">
      <svg width="40" height="40" viewBox="0 0 40 40" aria-hidden="true"><circle cx="20" cy="20" r="20" fill="#fefefe"/><rect x="10" y="13" width="20" height="14" rx="2" fill="#6cbd3e"/><path d="M10.5 14l9.5 7 9.5-7" stroke="#fefefe" stroke-width="2" fill="none"/></svg>
      <span>hello@bloomwell4kids.com</span>
    </div>
    <div class="contact-item web">
      <svg width="40" height="40" viewBox="0 0 40 40" aria-hidden="true"><circle cx="20" cy="20" r="20" fill="#fefefe"/><circle cx="20" cy="20" r="10" fill="none" stroke="#6cbd3e" stroke-width="2.5"/><ellipse cx="20" cy="20" rx="4.5" ry="10" fill="none" stroke="#6cbd3e" stroke-width="2"/><path d="M10 20h20M12 15h16M12 25h16" stroke="#6cbd3e" stroke-width="2"/></svg>
      <span>www.bloomwell4kids.com</span>
    </div>
  </footer>
</main>
</body>
</html>
```